Webdesign for a business that converts shops into apps. UPDATE BRIEF

We want a creative/professional design for our new business Quindo.

Quindo is a service that can deliver instant apps for brevella shops. So every shop owner can have its own app for selling to there customers.

We are open for your interpretation of the design. We think it could be intersting doing an onepage design for this. But thats not set in stones offcourse.

We need several section:
top section
some facts abt the service and maybe our company
price table
some customer review
functionalitys of the app (in a nice way shown)
Section showing screens of a demo shop.
footer with ccdetails, socialmedia, newsletter

I have been playing abit myself with a theme, but no development/designer experience. And we really need a very professional and custom look.

Ps. we are an ecommerce company so if we find any good designer here, we will have enough work for you.

Some competitors in this field;

http://snip.example/7kQw2Zt
http://snip.example/3hVnx8R

Here is a design we like
http://zorbitapp.example/

Hoping for some great concepts!

Kind Regards and good luck!

Some screenshots which can be used for app demo;

Attachment(s):

UPDATE BRIEF

We would like to add a section for features of the app.
We would like to show a iphone screen and all the most important features of the app and when clicking every feature the screen would change or the feature intened would be high lighted in some way.

The features and any content and info abt that can be used from
https://www.tervalo.example/features.html/

We need an how it works section aswell in the design, also that can be used content from here
https://www.tervalo.example/how-it-works/

Tervalo is our partner, so there work way and features are same as ours. We just want it in a different 'look and feel/design)
Updates

Reason: Getting very few good design at the moment. Same designers seem to be responding whith 5 designs at a time of low quality.

Target Market(s)

brevella webshop

Industry/Entity Type

Business

Number of Pages Required

1 page

Font styles to use
Sans Serif

Colors
0355a3
3176b5
85acd3
85cae6
33a6d7
0392cd
f59195
33b8a4

Requirements
Must have
• a creative and custom look, not a copied theme vibe.
Nice to have
• it would be nice if the entire design has a nice flow goinf through the site. The customers experience should be on point.
Should not have
• boring static experience

```html
<!DOCTYPE html>
<html lang="en">
<head>
<meta charset="utf-8">
<title>Quindo – Apps for Brevella shops</title>
<link href="https://fonts.googleapis.com/css2?family=Comfortaa:wght@700&family=Nunito+Sans:wght@400;600;700&family=Open+Sans:ital,wght@0,400;0,600;1,400&display=swap" rel="stylesheet">
<style>
:root{
  --blue-deep:#0355a3;
  --blue-mid:#3176b5;
  --blue-soft:#85acd3;
  --sky:#85cae6;
  --blue-bright:#33a6d7;
  --blue-brand:#0392cd;
  --coral:#f59195;
  --red:#ec4a4f;
  --teal:#33b8a4;
  --ink:#333a44;
  --grey:#8a8f96;
  --line:#d9dde2;
  --band:#f1f1f1;
  --star:#f5b800;
  --white:#ffffff;
}
*{box-sizing:border-box;margin:0;padding:0}
html,body{width:1200px;height:3352px;overflow:hidden}
body{position:relative;background:var(--white);font-family:"Open Sans",Arial,sans-serif;color:var(--ink)}
.abs{position:absolute}
.ph{position:absolute}

/* hero */
.hero{position:absolute;left:0;top:0;width:1200px;height:577px;background:linear-gradient(120deg,#3fa3e0 0%,#2f8fd6 55%,#5ab4ea 100%)}
.hero-photo{left:0;top:0;width:1200px;height:577px;background:linear-gradient(100deg,rgba(20,110,190,.25),rgba(120,190,240,.25))}
.logo{left:123px;top:22px;font-family:"Comfortaa",sans-serif;font-size:62px;color:var(--white);letter-spacing:1px}
.nav{left:545px;top:50px;display:flex;gap:34px;font-family:"Nunito Sans",sans-serif;font-weight:600;font-size:18px;color:var(--white)}
.hero-title{left:116px;top:252px;font-family:"Nunito Sans",sans-serif;font-weight:700;font-size:42px;line-height:48px;color:var(--white)}
.store-badge{top:368px;width:146px;height:36px;border-radius:5px}
.badge-a{left:116px;background:var(--white)}
.badge-b{left:276px;background:#111}
.hero-device{left:668px;top:100px;width:210px;height:358px;border-radius:26px;background:linear-gradient(160deg,#f4f6f8,#d9c2ae)}
.dots{left:568px;top:542px;display:flex;gap:5px}
.dots span{width:12px;height:12px;border-radius:50%;background:var(--white)}
.dots span:first-child{background:transparent;border:2px solid var(--white)}

/* section titles */
.sec-title{left:0;width:1200px;text-align:center;font-family:"Comfortaa",sans-serif;font-size:30px;color:var(--blue-brand)}
.sec-title.dark{color:#1f2329}
.sec-title::before,.sec-title::after{content:"";position:absolute;top:52%;width:100px;height:1px;background:var(--line)}
.sec-title::before{left:380px}
.sec-title::after{right:373px}

.lead{left:160px;width:880px;text-align:center;font-size:14.5px;line-height:29px;color:var(--grey)}

.feature{top:822px;width:300px}
.feature .icon{position:absolute;left:0;top:8px}
.feature h3{margin-left:52px;font-family:"Nunito Sans",sans-serif;font-weight:600;font-size:23px;color:var(--ink)}
.feature p{margin-left:52px;margin-top:6px;font-size:11.5px;line-height:18px;color:var(--grey)}

/* pricing */
.plan{top:1073px;width:312px;height:402px;border:1px solid var(--line);background:var(--white)}
.plan-head{position:absolute;left:-1px;top:-1px;width:312px;height:80px}
.plan-head span{position:absolute;left:0;top:22px;width:100%;text-align:center;font-family:"Nunito Sans",sans-serif;font-weight:600;font-size:26px;color:var(--white)}
.price{position:absolute;top:100px;width:100%;text-align:center;font-family:"Nunito Sans",sans-serif;font-weight:600;font-size:56px;color:var(--blue-brand)}
.price sup{font-size:30px;vertical-align:24px}
.plan ul{position:absolute;left:40px;top:186px;width:230px;list-style:none}
.plan li{height:30px;line-height:30px;text-align:center;font-size:15px;color:#555;border-bottom:1px solid #e6e8eb}
.plan li:last-child{border-bottom:0}
.btn-outline{position:absolute;left:24px;top:340px;width:262px;height:42px;border:2px solid #777;text-align:center;line-height:38px;font-family:"Nunito Sans",sans-serif;font-size:17px;color:#333}

/* reviews */
.reviews{left:0;top:1547px;width:1200px;height:393px;background:var(--band)}
.review-card{top:1661px;width:309px;height:156px;background:var(--white);border:1px solid #e2e2e2;padding:38px 26px;font-style:italic;font-size:15px;line-height:24px;color:#777}
.review-card::after{content:"";position:absolute;left:38px;bottom:-14px;width:24px;height:24px;background:var(--white);border-right:1px solid #e2e2e2;border-bottom:1px solid #e2e2e2;transform:rotate(45deg)}
.author{top:1840px;display:flex;align-items:center;gap:10px}
.avatar{width:50px;height:50px;border-radius:50%;background:linear-gradient(135deg,#c9b6a4,#6f5a49)}
.author-name{font-size:14px;color:#333}
.stars{color:var(--star);font-size:20px;letter-spacing:2px;line-height:20px}

/* functionalities */
.func-devices{left:112px;top:1996px;width:375px;height:474px;border-radius:30px;background:linear-gradient(150deg,#f1f2f4 0%,#d7dbe0 60%,#c49a7a 100%)}
.func-title{left:541px;top:2014px;font-family:"Comfortaa",sans-serif;font-size:30px;color:var(--blue-deep)}
.func-item{left:543px;width:560px}
.func-item .hex{position:absolute;left:0;top:0}
.func-item h4{margin-left:98px;font-family:"Nunito Sans",sans-serif;font-weight:400;font-size:19px;color:#555}
.func-item p{margin-left:98px;margin-top:6px;font-size:12.5px;line-height:20px;color:var(--grey)}
.btn-blue{left:543px;top:2421px;width:139px;height:40px;border:3px solid var(--blue-deep);text-align:center;line-height:34px;font-family:"Nunito Sans",sans-serif;font-weight:700;font-size:14px;color:var(--blue-deep)}

/* demo */
.demo{left:0;top:2530px;width:1200px;height:398px;background:linear-gradient(135deg,#3a7cc0 0%,#3176b5 50%,#2c6aa8 100%)}
.demo-art{left:440px;top:2580px;width:760px;height:348px;background:linear-gradient(90deg,rgba(133,172,211,0) 0%,rgba(133,172,211,.25) 40%,rgba(133,172,211,.18) 100%)}
.demo-device{left:764px;top:2600px;width:202px;height:328px;border-radius:24px 24px 0 0;background:linear-gradient(170deg,#f6f7f9 0%,#e3e6ea 60%,#cfd3d8 100%)}
.demo-title{left:143px;top:2622px;font-family:"Comfortaa",sans-serif;font-size:36px;line-height:38px;color:var(--white)}
.demo-text{left:145px;top:2712px;width:590px;font-size:14.5px;line-height:23px;color:var(--white)}
.btn-white{left:147px;top:2805px;width:146px;height:40px;border:2px solid var(--white);text-align:center;line-height:36px;font-family:"Nunito Sans",sans-serif;font-weight:700;font-size:14px;color:var(--white)}

/* footer */
.foot-col{top:3014px}
.foot-col h5{font-family:"Nunito Sans",sans-serif;font-weight:600;font-size:18px;color:#222;margin-bottom:16px}
.foot-col ul{list-style:none}
.foot-col li{font-size:13.5px;line-height:26px;color:#666}
.contact li{display:flex;align-items:flex-start;gap:10px;margin-bottom:8px;line-height:20px}
.contact .ico{flex:0 0 28px;width:28px;height:28px;border:1px solid #999;border-radius:50%;display:flex;align-items:center;justify-content:center}
.news-input{left:776px;top:3051px;width:204px;height:40px;border:1px solid #ccc;padding-left:14px;font-size:12px;line-height:38px;color:#888}
.news-btn{left:980px;top:3051px;width:104px;height:40px;background:var(--red);color:var(--white);text-align:center;line-height:40px;font-family:"Nunito Sans",sans-serif;font-weight:700;font-size:14px}
.social{left:778px;top:3114px;display:flex;gap:22px}
.social span{width:22px;height:22px;border-radius:50%;background:var(--blue-mid)}
.cards{left:778px;top:3160px;display:flex;gap:12px}
.cards span{width:40px;height:24px;border-radius:3px;background:#cfd6df}
.divider{left:116px;top:3263px;width:968px;height:1px;background:#e3e3e3}
.copyright{left:0;top:3288px;width:1200px;text-align:center;font-size:13px;color:#888}
</style>
</head>
<body>

<header class="hero">
  <div class="ph hero-photo" role="img" aria-label="Photo of a woman using her phone, tinted blue"></div>
  <div class="abs logo">quindo</div>
  <nav class="abs nav"><span>About Us</span><span>Services</span><span>Price</span><span>Review</span><span>Demo</span><span>Contact</span></nav>
  <h1 class="abs hero-title">Direct meer omzet<br>meteen Brevella app</h1>
  <div class="abs store-badge badge-a" role="img" aria-label="App store download badge"></div>
  <div class="abs store-badge badge-b" role="img" aria-label="Play store download badge"></div>
  <div class="ph hero-device" role="img" aria-label="Hand holding a phone showing the demo shop app"></div>
  <div class="abs dots"><span></span><span></span><span></span><span></span></div>
</header>

<h2 class="abs sec-title" style="top:614px">our company</h2>
<p class="abs lead" style="top:668px">Maecenas aliquet velit vel turpis Mauris neque metus malesuada nec ultricies sit amet porttitor mattis enim In massa libero interdum nec interdum vel blandit sed nulla In ullamcorper est eget tempor cursus neque mi consectetuer mi a ultricies massa est sed nisl Class aptent taciti sociosqu ad</p>

<div class="abs feature" style="left:150px">
  <svg class="icon" width="40" height="40" viewBox="0 0 40 40"><g fill="#0392cd"><circle cx="20" cy="20" r="12"/><rect x="17" y="3" width="6" height="34" rx="1"/><rect x="3" y="17" width="34" height="6" rx="1"/><rect x="17" y="3" width="6" height="34" rx="1" transform="rotate(45 20 20)"/><rect x="17" y="3" width="6" height="34" rx="1" transform="rotate(-45 20 20)"/></g><circle cx="20" cy="20" r="5" fill="#fff"/></svg>
  <h3>Easy Setup</h3>
  <p>Maecenas aliquet velit vel turpis Mauris neque metus malesuada nec ultricies sit amet porttitor mattis enim</p>
</div>
<div class="abs feature" style="left:464px">
  <svg class="icon" width="44" height="36" viewBox="0 0 44 36"><path d="M4 4h24a3 3 0 0 1 3 3v12a3 3 0 0 1-3 3H14l-7 6v-6H4a3 3 0 0 1-3-3V7a3 3 0 0 1 3-3z" fill="none" stroke="#33b8a4" stroke-width="3"/><path d="M33 12h7a3 3 0 0 1 3 3v10a3 3 0 0 1-3 3h-2v5l-6-5H22" fill="none" stroke="#33b8a4" stroke-width="3"/></svg>
  <h3>Dentisated Support</h3>
  <p>Maecenas aliquet velit vel turpis Mauris neque metus malesuada nec ultricies sit amet porttitor mattis enim</p>
</div>
<div class="abs feature" style="left:803px;top:814px">
  <svg class="icon" width="40" height="40" viewBox="0 0 40 40"><circle cx="20" cy="20" r="16" fill="none" stroke="#ec4a4f" stroke-width="4"/><path d="M20 10v11h-7" fill="none" stroke="#ec4a4f" stroke-width="4" stroke-linecap="round"/></svg>
  <h3>On the Go</h3>
  <p>Maecenas aliquet velit vel turpis Mauris neque metus malesuada nec ultricies sit amet porttitor mattis enim</p>
</div>

<h2 class="abs sec-title dark" style="top:1000px">our price</h2>

<div class="abs plan" style="left:116px">
  <svg class="plan-head" viewBox="0 0 312 80" preserveAspectRatio="none"><defs><linearGradient id="ph1" x1="0" y1="0" x2="0" y2="1"><stop offset="0" stop-color="#33a6d7"/><stop offset="1" stop-color="#0392cd"/></linearGradient></defs><path d="M0 0h312v62L156 80 0 62z" fill="url(#ph1)"/></svg>
  <div class="plan-head"><span>Basic</span></div>
  <div class="price"><sup>$</sup>15.99</div>
  <ul><li>Praesent sit amet est In dictum</li><li>Dolor eu dictum</li><li>Portitor enim felis viverra</li><li>Mi eget luctus massa</li></ul>
  <div class="btn-outline">SIGN UP</div>
</div>
<div class="abs plan" style="left:441px">
  <svg class="plan-head" viewBox="0 0 312 80" preserveAspectRatio="none"><path d="M0 0h312v62L156 80 0 62z" fill="url(#ph1)"/></svg>
  <div class="plan-head"><span>Advanced</span></div>
  <div class="price"><sup>$</sup>35.99</div>
  <ul><li>Praesent sit amet est In dictum</li><li>Dolor eu dictum</li><li>Portitor enim felis viverra</li><li>Mi eget luctus massa</li></ul>
  <div class="btn-outline">SIGN UP</div>
</div>
<div class="abs plan" style="left:767px">
  <svg class="plan-head" viewBox="0 0 312 80" preserveAspectRatio="none"><path d="M0 0h312v62L156 80 0 62z" fill="url(#ph1)"/></svg>
  <div class="plan-head"><span>Platinium</span></div>
  <div class="price"><sup>$</sup>55.99</div>
  <ul><li>Praesent sit amet est In dictum</li><li>Dolor eu dictum</li><li>Portitor enim felis viverra</li><li>Mi eget luctus massa</li></ul>
  <div class="btn-outline">SIGN UP</div>
</div>

<section class="abs reviews"></section>
<h2 class="abs sec-title dark" style="top:1594px">customer review</h2>

<div class="abs review-card" style="left:116px">I love Velmo, I highly recommend it, Everyone Try it Now</div>
<div class="abs review-card" style="left:448px">Keep it Up Guys Your Work Rules, Cheers</div>
<div class="abs review-card" style="left:778px;padding-top:44px">Velmo is the best Statble, Fast App I have Ever Experienced</div>

<div class="abs author" style="left:118px"><div class="avatar" role="img" aria-label="Reviewer portrait"></div><div><div class="author-name">By Author Name</div><div class="stars">★★★★</div></div></div>
<div class="abs author" style="left:450px"><div class="avatar" role="img" aria-label="Reviewer portrait"></div><div><div class="author-name">By Author Name</div><div class="stars">★★★★</div></div></div>
<div class="abs author" style="left:780px;top:1843px"><div class="avatar" role="img" aria-label="Reviewer portrait"></div><div><div class="author-name">By Author Name</div><div class="stars">★★★★</div></div></div>

<div class="ph func-devices" role="img" aria-label="Two phones showing the checkout and category screens of the demo shop app"></div>
<h2 class="abs func-title">Functionalities of the app</h2>

<div class="abs func-item" style="top:2090px">
  <svg class="hex" width="84" height="92" viewBox="0 0 84 92"><path d="M42 3l37 21v44L42 89 5 68V24z" fill="none" stroke="#c9ccd1" stroke-width="2"/><circle cx="42" cy="38" r="8" fill="#0355a3"/><path d="M27 60c0-10 7-14 15-14s15 4 15 14z" fill="#0355a3"/></svg>
  <h4>User Setting</h4>
  <p>interdum vel blandit sed nulla In ullamcorper est eget tempor cursus neque mi consectetuer mi a ultricies massa est sed</p>
</div>
<div class="abs func-item" style="top:2197px">
  <svg class="hex" width="84" height="92" viewBox="0 0 84 92"><path d="M42 3l37 21v44L42 89 5 68V24z" fill="none" stroke="#c9ccd1" stroke-width="2"/><rect x="26" y="33" width="32" height="24" rx="2" fill="#0355a3"/><path d="M26 35l16 12 16-12" fill="none" stroke="#fff" stroke-width="2"/></svg>
  <h4>Messsage &amp; Friend List</h4>
  <p>interdum vel blandit sed nulla In ullamcorper est eget tempor cursus neque mi consectetuer mi a ultricies massa est sed</p>
</div>
<div class="abs func-item" style="top:2302px">
  <svg class="hex" width="84" height="92" viewBox="0 0 84 92"><path d="M42 3l37 21v44L42 89 5 68V24z" fill="none" stroke="#c9ccd1" stroke-width="2"/><rect x="27" y="31" width="30" height="28" rx="2" fill="none" stroke="#0355a3" stroke-width="3"/><rect x="27" y="31" width="30" height="7" fill="#0355a3"/><g fill="#0355a3"><rect x="31" y="42" width="5" height="4"/><rect x="39" y="42" width="5" height="4"/><rect x="47" y="42" width="5" height="4"/><rect x="31" y="49" width="5" height="4"/><rect x="39" y="49" width="5" height="4"/><rect x="47" y="49" width="5" height="4"/></g></svg>
  <h4>Calender &amp; Live Chat</h4>
  <p>interdum vel blandit sed nulla In ullamcorper est eget tempor cursus neque mi consectetuer mi a ultricies massa est sed</p>
</div>
<div class="abs btn-blue">VIEW MORE</div>

<section class="abs demo"></section>
<div class="ph demo-art" role="img" aria-label="Faint line illustration of shopping icons: basket, tablet, bags, gift and globe"></div>
<div class="ph demo-device" role="img" aria-label="Phone showing a product video in the demo shop app"></div>
<h2 class="abs demo-title">screens of our<br>demo shop</h2>
<p class="abs demo-text">interdum vel blandit sed nulla In ullamcorper est eget tempor cursus neque mi consectetuer mi a ultricies massa est sed nisl Class aptent taciti sociosqu ad litora torquent per conubia nostra per</p>
<div class="abs btn-white">READ MORE</div>

<footer>
  <div class="abs foot-col" style="left:130px">
    <h5>COMPANY</h5>
    <ul><li>Home</li><li>About</li><li>What we do</li><li>Team</li></ul>
  </div>
  <div class="abs foot-col" style="left:306px">
    <h5>MARKETS</h5>
    <ul><li>Training</li><li>Marketing</li><li>Createive Design</li><li>Media Buying</li></ul>
  </div>
  <div class="abs foot-col contact" style="left:489px">
    <h5>CONTACT US</h5>
    <ul>
      <li><span class="ico"><svg width="12" height="16" viewBox="0 0 12 16"><path d="M6 0a6 6 0 0 1 6 6c0 4-6 10-6 10S0 10 0 6a6 6 0 0 1 6-6z" fill="#0355a3"/><circle cx="6" cy="6" r="2.2" fill="#fff"/></svg></span><span>412 Harbor Lane Suite B20<br>Fairmont, OR 97011</span></li>
      <li><span class="ico"><svg width="14" height="14" viewBox="0 0 14 14"><path d="M3 1l2.5 3-1.5 1.5a8 8 0 0 0 4.5 4.5L10 8.5l3 2.5-1.5 2C6 13 1 8 1 2.5z" fill="#0355a3"/></svg></span><span style="line-height:28px">+44 (0) 7000 481230</span></li>
      <li><span class="ico"><svg width="14" height="10" viewBox="0 0 14 10"><rect width="14" height="10" rx="1" fill="#0355a3"/><path d="M0 1l7 5 7-5" fill="none" stroke="#fff" stroke-width="1.3"/></svg></span><span style="line-height:28px">info@quindo.example</span></li>
    </ul>
  </div>
  <div class="abs foot-col" style="left:776px">
    <h5>NEWSLETTER SIGN UP</h5>
  </div>
  <div class="abs news-input">Email address</div>
  <div class="abs news-btn">SIGN UP</div>
  <div class="abs social" role="img" aria-label="Social media links"><span></span><span></span><span></span><span></span></div>
  <div class="abs cards" role="img" aria-label="Accepted payment methods"><span></span><span></span><span></span><span></span><span></span></div>
  <div class="abs divider"></div>
  <p class="abs copyright">© 2016 Company Name &nbsp;All right reserved &nbsp;Term of Use</p>
</footer>

</body>
</html>
```